KTR Civils*

we are a construction company specialising in Housing, Water Infrastructure and Roadworks
This is the description I would like to be added to the Flyer. I have
also attached a Picture
Ktr Civils is a Construction Company specializing in Housing, Roadworks
and Water infrastructure. Ktr has established itself firmly in the
Construction industry with branches all through Southern Africa as well
as into Africa.
Ktr is committed to giving its Clients efficient and Professional
service at all times, We pride ourselves on our ability to meet
deadlines and exceed expectations. Our aim is to establish Successful
Long lasting relationships with our Client base
Colors
Designer to choose only greyscale colors for use in the design.
Look and feel

```html
<!DOCTYPE html>
<html lang="en">
<head>
<meta charset="utf-8">
<title>KTR Civils Flyer</title>
<link href="https://fonts.googleapis.com/css2?family=Open+Sans:wght@400;600;700&display=swap" rel="stylesheet">
<style>
  :root {
    --stage: #4a4a4a;
    --paper: #000000;
    --ink: #ffffff;
    --red: #d8121c;
    --orange: #f26a0c;
    --yellow: #ffc400;
    --sky: #c9d3dc;
    --hill: #6f7f8a;
    --roof: #c9684f;
    --grass: #8a9a5a;
  }
  * { margin: 0; padding: 0; box-sizing: border-box; }
  html, body {
    width: 1200px;
    height: 800px;
    overflow: hidden;
    background: var(--stage);
    font-family: "Open Sans", sans-serif;
  }
  .flyer {
    position: absolute;
    left: 330px;
    top: 18px;
    width: 540px;
    height: 764px;
    background: var(--paper);
    color: var(--ink);
    overflow: hidden;
  }
  .brand {
    position: absolute;
    top: 48px;
    left: 0;
    width: 100%;
    display: flex;
    justify-content: center;
    align-items: center;
    gap: 14px;
  }
  .brand-mark {
    width: 34px;
    height: 34px;
    background: var(--red);
  }
  .brand-name {
    font-size: 52px;
    font-weight: 700;
    color: var(--ink);
    letter-spacing: 1px;
  }
  .services {
    position: absolute;
    top: 132px;
    left: 0;
    width: 100%;
    display: flex;
    justify-content: center;
    font-size: 15px;
    font-weight: 600;
    letter-spacing: 0.5px;
    text-transform: uppercase;
  }
  .services span + span {
    border-left: 1px solid var(--ink);
    margin-left: 10px;
    padding-left: 10px;
  }
  .hero-photo {
    position: absolute;
    top: 190px;
    left: 0;
    width: 100%;
    height: 290px;
    background: linear-gradient(180deg, var(--sky) 0%, var(--hill) 30%, var(--roof) 55%, #cbb892 72%, var(--grass) 100%);
  }
  .title-band {
    position: absolute;
    top: 440px;
    left: 0;
    width: 100%;
    height: 72px;
  }
  .title-band svg { display: block; }
  .title {
    position: absolute;
    top: 448px;
    left: 40px;
    font-size: 40px;
    font-weight: 400;
    color: var(--ink);
  }
  .about {
    position: absolute;
    top: 532px;
    left: 44px;
    width: 340px;
    font-size: 12.5px;
    line-height: 1.4;
  }
  .about p + p { margin-top: 16px; }
  .service-icons {
    position: absolute;
    top: 456px;
    right: 36px;
    display: flex;
    flex-direction: column;
    gap: 32px;
  }
  .service-icon {
    width: 66px;
    height: 66px;
    border-radius: 50%;
    background: linear-gradient(135deg, var(--orange), var(--red));
    display: flex;
    align-items: center;
    justify-content: center;
  }
  .service-icon svg {
    width: 36px;
    height: 36px;
    fill: none;
    stroke: var(--ink);
    stroke-width: 2;
    stroke-linejoin: round;
    stroke-linecap: round;
  }
</style>
</head>
<body>
  <main class="flyer">
    <header class="brand">
      <div class="brand-mark"></div>
      <div class="brand-name">KTR Civils</div>
    </header>
    <div class="services">
      <span>Housing</span><span>Water Infrastructure</span><span>Roadworks</span>
    </div>

    <div class="hero-photo" role="img" aria-label="Photograph of a new housing development with rows of small houses, power lines and hills behind"></div>

    <div class="title-band">
      <svg width="540" height="72" viewBox="0 0 540 72">
        <defs>
          <linearGradient id="bandFade" x1="0" x2="1" y1="0" y2="0">
            <stop offset="0" stop-color="#f26a0c"/>
            <stop offset="1" stop-color="#ffc400"/>
          </linearGradient>
        </defs>
        <polygon points="0,14 540,0 540,30 0,72" fill="url(#bandFade)"/>
        <polygon points="0,14 300,6 280,72 0,72" fill="#d8121c"/>
      </svg>
    </div>
    <h1 class="title">Ktr Civils</h1>

    <section class="about">
      <p>Ktr Civils is a Construction Company specializing in Housing, Roadworks and Water infrastructure. Ktr has established itself firmly in the Construction industry with branches all through Southern Africa as well as into Africa.</p>
      <p>Ktr is committed to giving its Clients efficient and Professional service at all times, We pride ourselves on our ability to meet deadlines and exceed expectations. Our aim is to establish Successful Long lasting relationships with our Client base</p>
    </section>

    <aside class="service-icons">
      <div class="service-icon" aria-label="Housing">
        <svg viewBox="0 0 36 36"><path d="M4 18 L18 6 L32 18"/><path d="M8 15 V31 H28 V15"/><rect x="14" y="21" width="8" height="10"/></svg>
      </div>
      <div class="service-icon" aria-label="Water infrastructure">
        <svg viewBox="0 0 36 36"><path d="M18 5 C12 14 9 18 9 23 A9 9 0 0 0 27 23 C27 18 24 14 18 5 Z"/></svg>
      </div>
      <div class="service-icon" aria-label="Roadworks">
        <svg viewBox="0 0 36 36"><path d="M12 4 L4 32"/><path d="M24 4 L32 32"/><path d="M18 6 V11"/><path d="M18 16 V21"/><path d="M18 26 V31"/></svg>
      </div>
    </aside>
  </main>
</body>
</html>
```